Business Cards for our company

Hi there,

we have successfully designed a logo with ArtFlock and would like now to design our business cards. We would like to keep the colours and the look-and-feel of the logo. Please send in variations with two or three colours and one or two sides. I promise to respond to every single submission.

Many thanks and happy new year.

All the best,
Wilfried

Target Market(s)

B2B

Industry/Entity Type

Trade

Contact Information for Business Card

We have successfully designed a logo with ArtFlock and would like now to design our business cards. We would like to keep the colours and the look-and-feel of the logo. Please send in variations with two or three colours and one or two sides. I promise to respond to every single submission.

Font styles to use
Serif
Sans Serif
Script

Requirements
Must have
• These information should be on the business card, grouped as you suggest, and we think using small pictograms for mobile, email, etc is pretty helpful:
• Wilfried Tammler (first and second name)
• Geschäftsführer/ Managing Director (title)
• KoR Warenkontor GmbH (company name and legal form)
• Ostheimer Str. 18/3 (street and house number)
• 70839 Gerlingen (zip code and town)
• +491709384562 (mobile)
• +4971569027341 (work)
• w.tammler@kor-warenkontor.example (email)
• www.kor-warenkontor.example (web)
Nice to have
• Spectacular and interesting layout and design. You look at it and think, wow, that's not the normal stuff.
• We think of ourselves as bridge-builders between businesses (international producers on the one hand, and retail chains on the other hand) and we translate, organise and manage projects where both partners are involved, but it's difficult for them to cooperate due to language barriers and different working cultures.
• This is why we have the n between the B's shaped as a bridge, and the green arc supports this idea. Maybe you could play with this idea...
Should not have
• the standard layout that everybody has

```html
<!DOCTYPE html>
<html lang="de">
<head>
<meta charset="utf-8">
<title>KoR Warenkontor – Visitenkarten</title>
<link rel="stylesheet" href="https://fonts.googleapis.com/css2?family=Open+Sans:wght@400;600;700&display=swap">
<style>
  :root {
    --backdrop: #2a2a2a;
    --card-white: #ffffff;
    --ink-black: #111111;
    --brand-green: #2eaa45;
    --navy: #173a4a;
    --charcoal: #333436;
    --grey-text: #6a6a6a;
    --light-text: #f2f2f2;
  }
  * { box-sizing: border-box; margin: 0; padding: 0; }
  html, body { width: 1200px; height: 1000px; overflow: hidden; }
  body {
    background: var(--backdrop);
    font-family: "Open Sans", Arial, sans-serif;
    position: relative;
  }
  .card {
    position: absolute;
    left: 250px;
    width: 700px;
    height: 400px;
    border-radius: 28px;
    background: var(--card-white);
    overflow: hidden;
    box-shadow: 0 14px 30px rgba(0,0,0,.45);
  }
  .card--front { top: 60px; }
  .card--back { top: 540px; }

  .wordmark {
    display: flex;
    align-items: center;
    gap: 14px;
    font-weight: 700;
    color: var(--ink-black);
    letter-spacing: -2px;
  }
  .wordmark__dot {
    border-radius: 50%;
    background: var(--brand-green);
    flex: none;
  }
  .card--front .wordmark {
    position: absolute;
    left: 0; right: 0; top: 110px;
    justify-content: center;
    font-size: 120px;
    line-height: 1;
  }
  .card--front .wordmark__dot { width: 34px; height: 34px; }
  .company-line {
    position: absolute;
    left: 0; right: 0; top: 262px;
    text-align: center;
    font-size: 15px;
    color: var(--grey-text);
  }

  .card--back .wordmark {
    position: absolute;
    left: 50px; top: 40px;
    font-size: 72px;
    line-height: 1;
  }
  .card--back .wordmark__dot { width: 22px; height: 22px; }
  .person {
    position: absolute;
    right: 48px; top: 40px;
    text-align: right;
  }
  .person__name {
    font-size: 26px;
    font-weight: 600;
    color: var(--navy);
    letter-spacing: .5px;
    line-height: 1.1;
  }
  .person__title {
    font-size: 17px;
    font-weight: 600;
    color: var(--brand-green);
    letter-spacing: .5px;
  }
  .person__address {
    margin-top: 14px;
    font-size: 14px;
    color: var(--grey-text);
  }
  .swoosh {
    position: absolute;
    left: 0; top: 0;
    width: 700px; height: 400px;
  }
  .contact-list {
    position: absolute;
    left: 50px; bottom: 24px;
    list-style: none;
    color: var(--light-text);
    font-size: 17px;
    line-height: 26px;
  }
  .contact-list li { display: flex; align-items: center; gap: 14px; }
  .contact-list svg { width: 15px; height: 15px; flex: none; fill: var(--brand-green); }
  .accent { color: var(--brand-green); }
</style>
</head>
<body>
  <section class="card card--front" aria-label="Visitenkarte Vorderseite">
    <div class="wordmark"><span>KoR</span><span class="wordmark__dot"></span></div>
    <p class="company-line">KoR Warenkontor GmbH</p>
  </section>

  <section class="card card--back" aria-label="Visitenkarte Rückseite">
    <svg class="swoosh" viewBox="0 0 700 400" aria-hidden="true">
      <path d="M0 232 C220 182 450 150 700 142 L700 400 L0 400 Z" fill="var(--brand-green)"/>
      <path d="M0 250 C220 200 450 168 700 160 L700 400 L0 400 Z" fill="var(--charcoal)"/>
    </svg>

    <div class="wordmark"><span>KoR</span><span class="wordmark__dot"></span></div>

    <div class="person">
      <p class="person__name">WILFRIED TAMMLER</p>
      <p class="person__title">MANAGING DIRECTOR</p>
      <p class="person__address">Ostheimer Str. 18/3, 70839 Gerlingen</p>
    </div>

    <ul class="contact-list">
      <li>
        <svg viewBox="0 0 24 24"><path d="M6.6 10.8a15 15 0 0 0 6.6 6.6l2.2-2.2a1 1 0 0 1 1-.25 11.4 11.4 0 0 0 3.6.57 1 1 0 0 1 1 1V20a1 1 0 0 1-1 1A17 17 0 0 1 3 4a1 1 0 0 1 1-1h3.5a1 1 0 0 1 1 1c0 1.25.2 2.45.57 3.57a1 1 0 0 1-.25 1z"/></svg>
        <span>+491709384562</span>
      </li>
      <li>
        <svg viewBox="0 0 24 24"><rect x="2" y="4" width="20" height="4" rx="2"/><rect x="2" y="7" width="5" height="4" rx="1"/><rect x="17" y="7" width="5" height="4" rx="1"/><rect x="5" y="11" width="14" height="10" rx="2"/></svg>
        <span>+4971569027341</span>
      </li>
      <li>
        <svg viewBox="0 0 24 24"><path d="M2 5h20v14H2zm2 2v.5l8 5.5 8-5.5V7z"/></svg>
        <span>w.tammler@kor-warenkontor.example</span>
      </li>
      <li>
        <svg viewBox="0 0 24 24"><circle cx="12" cy="12" r="10"/></svg>
        <span>www.<span class="accent">kor-warenkontor</span>.example</span>
      </li>
    </ul>
  </section>
</body>
</html>
```